Business Card Design Project

Looking for a square business card, 2"-2.5", with rounded corners. We specialize in exciting promotions with prize giveaways and our logo is attached.

I'm a fan of the sample card found here:
http://www.brimlacework.com/25-X-25-Rounded-Corner-Business-Cards_p_204.html

Business card should show Name, Phone #, Email, Title and website.

Two design possibilities:
1. QR code on one side (we will determine what it is later, any QR code can be used for the design), with logo and info on the other side. It might be too hard to fit everything in this way.
2. Logo on one side, info on the other.

Flexible on our final choice, but looking to see some designs with a scannable QR code on one side and some without.

Sample details
Name: Moss Darrow
Phone: +1(416)555-0187
Email: mossdarrow@tulvenquay.com
Website: http://tulvenquay.com

Target Market(s)

Internet startups

Industry/Entity Type

Business

Requirements
Must have
• Square design, most likely rounded corners
Nice to have
• QR code on one side, but seems like it would be hard to fit everything.

```html
<!DOCTYPE html>
<html lang="en">
<head>
<meta charset="utf-8">
<title>Moss Darrow – Business Card</title>
<link rel="stylesheet" href="https://fonts.googleapis.com/css2?family=Ubuntu:wght@400;500;700&display=swap">
<style>
  :root {
    --stage: #000000;
    --card-dark: #bd4a17;
    --card-glow: #f2a300;
    --panel: #ffffff;
    --accent-purple: #8e4a86;
    --ink: #111111;
    --name: #ffffff;
    --rule: #ffffff;
    --brand: #f6d21c;
  }
  html, body {
    margin: 0;
    padding: 0;
    width: 1200px;
    height: 849px;
    overflow: hidden;
    background: var(--stage);
    font-family: "Ubuntu", sans-serif;
  }
  .stage {
    position: relative;
    width: 1200px;
    height: 849px;
  }
  .card {
    position: absolute;
    width: 386px;
    height: 386px;
    border-radius: 46px;
    overflow: hidden;
    background:
      radial-gradient(ellipse 55% 45% at 58% 98%, var(--card-glow) 0%, rgba(242,163,0,0.85) 35%, rgba(242,163,0,0) 100%),
      var(--card-dark);
  }
  .card--front { left: 192px; top: 261px; }
  .card--back {
    left: 603px;
    top: 226px;
    width: 378px;
    height: 378px;
    transform: rotate(-8deg);
  }

  .holder-name {
    position: absolute;
    left: 60px;
    top: 32px;
    margin: 0;
    font-size: 33px;
    font-weight: 400;
    color: var(--name);
    letter-spacing: 0.3px;
  }
  .info-band {
    position: absolute;
    left: 0;
    top: 100px;
    width: 386px;
    height: 188px;
  }
  .info-band svg { display: block; }
  .contact-list {
    position: absolute;
    left: 60px;
    top: 161px;
    margin: 0;
    padding: 0;
    list-style: none;
    font-size: 17.5px;
    line-height: 19.5px;
    color: var(--ink);
  }
  .contact-list li {
    display: flex;
    align-items: center;
  }
  .contact-list .icon {
    width: 11px;
    height: 11px;
    margin-right: 18px;
    flex: none;
  }

  .back-rules {
    position: absolute;
    inset: 0;
  }
  .brand-name {
    position: absolute;
    left: 0;
    right: 0;
    top: 126px;
    margin: 0;
    text-align: center;
    font-size: 50px;
    line-height: 52px;
    font-weight: 700;
    color: var(--brand);
  }
</style>
</head>
<body>
<main class="stage">

  <section class="card card--front" aria-label="Card front with contact details">
    <h1 class="holder-name">Moss Darrow</h1>

    <div class="info-band">
      <svg width="386" height="188" viewBox="0 0 386 188">
        <defs>
          <linearGradient id="stripe" x1="0" x2="1" y1="0" y2="0">
            <stop offset="0" stop-color="#8e4a86"/>
            <stop offset="0.15" stop-color="#8e4a86"/>
            <stop offset="0.3" stop-color="#d83a7c"/>
            <stop offset="0.5" stop-color="#4a7fc4"/>
            <stop offset="0.7" stop-color="#c64a9a"/>
            <stop offset="0.9" stop-color="#3aa0c8"/>
          </linearGradient>
        </defs>
        <polygon points="0,0 349,0 295,188 0,188" fill="var(--panel)"/>
        <polygon points="0,0 349,0 345,13 0,13" fill="url(#stripe)" role="img" aria-label="Multicoloured stripe band"/>
        <polygon points="0,175 298,175 295,188 0,188" fill="url(#stripe)" role="img" aria-label="Multicoloured stripe band"/>
        <path d="M26 12 H40 V103 a7 7 0 0 1 -14 0 Z" fill="var(--accent-purple)"/>
      </svg>
    </div>

    <ul class="contact-list">
      <li>
        <svg class="icon" viewBox="0 0 12 12" aria-hidden="true"><path d="M2.5 1 L4.5 1 L5.3 3.4 L4 4.4 C4.6 5.8 6.2 7.4 7.6 8 L8.6 6.7 L11 7.5 L11 9.5 C11 10.3 10.3 11 9.5 11 C5 11 1 7 1 2.5 C1 1.7 1.7 1 2.5 1 Z" fill="#222"/></svg>
        <span>+1(416)555-0187</span>
      </li>
      <li>
        <svg class="icon" viewBox="0 0 12 12" aria-hidden="true"><rect x="0.5" y="2" width="11" height="8" fill="#222"/><path d="M1 2.5 L6 6.5 L11 2.5" stroke="#fff" stroke-width="1.2" fill="none"/></svg>
        <span>mossdarrow@tulvenquay.com</span>
      </li>
      <li>
        <svg class="icon" viewBox="0 0 12 12" aria-hidden="true"><circle cx="6" cy="6" r="5" fill="none" stroke="#222" stroke-width="1.3"/><path d="M1 6 H11 M6 1 C3.5 3.5 3.5 8.5 6 11 M6 1 C8.5 3.5 8.5 8.5 6 11" stroke="#222" stroke-width="1" fill="none"/></svg>
        <span>http://tulvenquay.com</span>
      </li>
    </ul>
  </section>

  <section class="card card--back" aria-label="Card back with brand name">
    <svg class="back-rules" width="378" height="378" viewBox="0 0 378 378" aria-hidden="true">
      <line x1="-2" y1="36" x2="124" y2="380" stroke="var(--rule)" stroke-width="3"/>
      <line x1="307" y1="-2" x2="321" y2="380" stroke="var(--rule)" stroke-width="3"/>
    </svg>
    <p class="brand-name">Tulven<br>Quay</p>
  </section>

</main>
</body>
</html>
```